New Business card with our new logo

NEW BUSINESS CARDS wth our new logo

Want a sophisticated look. Probably in deep purple ink. (but we are open)
Would like something that looks expensive. Do not want a cutsie food look.
Not sure what more information I can offer. If you have any please contact me.

NAME - Ruth Delacroix Hale, Owner
415-273 0918
ruth@velvetplatterco.example
velvetplatterco.example

Target Market(s)

not sure what your are asking?

Industry/Entity Type

Business

Contact Information for Business Card

Logo + informaiton
Want a sophisticated look if possible. The cards are for women

Font styles to use
Serif

Colors
886aae

Requirements
Must have
• Ruth Delacroix Hale, Owner
• 415-273 0918
• ruth@velvetplatterco.example
• velvetplatterco.example
Nice to have
• suprise me
Should not have
• No cute food images, chef hat, knives, forks, etc.

```html
<!DOCTYPE html>
<html lang="en">
<head>
<meta charset="utf-8">
<title>Velvet Platter – Business Card</title>
<link rel="stylesheet" href="https://fonts.googleapis.com/css2?family=Montserrat:wght@400&family=Open+Sans:wght@400&display=swap">
<style>
  :root {
    --stage: #181818;
    --card-white: #ffffff;
    --plum: #644179;
    --plum-ink: #5b2d6e;
    --leaf: #7dc242;
    --text-dark: #2a2a2a;
    --white: #ffffff;
  }
  html, body {
    margin: 0;
    padding: 0;
    width: 1200px;
    height: 900px;
    overflow: hidden;
    background: var(--stage);
  }
  .stage {
    position: relative;
    width: 1200px;
    height: 900px;
  }
  .card {
    position: absolute;
    top: 306px;
    width: 438px;
    height: 270px;
    border-radius: 10px;
    overflow: hidden;
    background: var(--plum);
  }
  .card--front { left: 150px; }
  .card--back { left: 609px; width: 440px; height: 272px; }

  .front-top {
    position: absolute;
    left: 0; top: 0;
    width: 100%;
    height: 127px;
    background: var(--card-white);
  }
  .front-rule {
    position: absolute;
    left: 0; top: 127px;
    width: 100%;
    height: 5px;
    background: var(--leaf);
  }

  .brand-name {
    margin: 0;
    font-family: "Montserrat", sans-serif;
    font-weight: 400;
    white-space: nowrap;
    letter-spacing: 0.5px;
  }
  .card--front .brand-name {
    position: absolute;
    left: 28px; top: 49px;
    font-size: 22px;
    line-height: 26px;
    color: var(--plum-ink);
  }
  .card--back .brand-name {
    position: absolute;
    left: 0; right: 0; top: 116px;
    text-align: center;
    font-size: 33px;
    line-height: 40px;
    color: var(--white);
  }

  .holder {
    position: absolute;
    right: 30px; top: 51px;
    text-align: right;
  }
  .holder-name {
    margin: 0;
    font-family: "Open Sans", sans-serif;
    font-size: 14px;
    color: var(--plum-ink);
    text-transform: uppercase;
    line-height: 18px;
  }
  .holder-role {
    margin: 0;
    font-family: "Open Sans", sans-serif;
    font-size: 13px;
    color: var(--text-dark);
    line-height: 18px;
  }

  .contact-list {
    position: absolute;
    left: 28px; top: 176px;
    margin: 0; padding: 0;
    list-style: none;
  }
  .contact-item {
    display: flex;
    align-items: center;
    height: 20px;
    font-family: "Open Sans", sans-serif;
    font-size: 15px;
    color: var(--white);
  }
  .contact-icon {
    width: 11px; height: 11px;
    margin-right: 7px;
    fill: var(--white);
  }
</style>
</head>
<body>
<main class="stage">
  <section class="card card--front" aria-label="Business card front">
    <div class="front-top"></div>
    <div class="front-rule"></div>
    <p class="brand-name">VELVET PLATTER</p>
    <div class="holder">
      <p class="holder-name">Ruth Delacroix Hale</p>
      <p class="holder-role">Owner</p>
    </div>
    <ul class="contact-list">
      <li class="contact-item">
        <svg class="contact-icon" viewBox="0 0 24 24" aria-hidden="true"><path d="M6.6 10.8c1.4 2.8 3.8 5.1 6.6 6.6l2.2-2.2c.3-.3.7-.4 1-.2 1.1.4 2.3.6 3.6.6.6 0 1 .4 1 1V20c0 .6-.4 1-1 1C10.6 21 3 13.4 3 4c0-.6.4-1 1-1h3.5c.6 0 1 .4 1 1 0 1.3.2 2.5.6 3.6.1.3 0 .7-.2 1L6.6 10.8z"/></svg>
        415-273 0918
      </li>
      <li class="contact-item">
        <svg class="contact-icon" viewBox="0 0 24 24" aria-hidden="true"><rect x="2" y="5" width="20" height="14"/><path d="M3 6.5l9 7 9-7" stroke="#644179" stroke-width="2" fill="none"/></svg>
        ruth@velvetplatterco.example
      </li>
      <li class="contact-item">
        <svg class="contact-icon" viewBox="0 0 24 24" aria-hidden="true"><circle cx="12" cy="12" r="11"/><path d="M7 6c2 1 3 3 2 5s1 3 2 5-1 4-2 5M15 4c-1 2 1 3 3 4" stroke="#644179" stroke-width="2" fill="none"/></svg>
        www.velvetplatterco.example
      </li>
    </ul>
  </section>

  <section class="card card--back" aria-label="Business card back">
    <p class="brand-name">VELVET PLATTER</p>
  </section>
</main>
</body>
</html>
```